Enterprise image desing

The designs are for a fashion store for young men and women.
Updates

Los diseƱos parecen similares

Target Market(s)

Young

Font styles to use
Sans Serif

Colors
ec1f27
ffffff
1b1b1b

Requirements
Must have
• Use clean and modern sources
Nice to have
• n / a
Should not have
• n / a

```html
<!DOCTYPE html>
<html lang="en">
<head>
<meta charset="utf-8">
<title>Veltaro stationery set</title>
<link href="https://fonts.googleapis.com/css2?family=Poppins:wght@700&family=Arimo:wght@400;700&display=swap" rel="stylesheet">
<style>
:root{
  --red:#e2202e;
  --red-soft:#e63a45;
  --red-deep:#d4232f;
  --ink:#14213d;
  --white:#ffffff;
  --blush:#fbe6e4;
  --mist:#e1e2e6;
  --stage:#d1cfd2;
}
*{margin:0;padding:0;box-sizing:border-box}
html,body{width:1189px;height:1200px;overflow:hidden;background:var(--stage)}
body{position:relative;font-family:"Arimo",Arial,sans-serif;color:var(--ink)}
.piece{position:absolute;overflow:hidden}
.brand{position:absolute;display:flex;align-items:center;font-family:"Poppins",Arial,sans-serif;font-weight:700;letter-spacing:.5px;white-space:nowrap}
.brand .dot{display:inline-block;background:var(--red);margin-right:.3em}
.brand.on-red{color:var(--white)}
.brand.on-red .dot{background:var(--white)}
.brand.on-white{color:var(--ink)}
.panel{position:absolute}
.contact{position:absolute;border-left:1.5px solid var(--ink);padding-left:6px;line-height:1.25;color:var(--ink)}
.contact .row{display:flex;align-items:center;gap:3px}
.ico{fill:var(--red);flex:none}
.bands{position:absolute;left:0;right:0;bottom:0}
.bands .thin{position:absolute;left:0;right:0;background:var(--red)}
.bands .thick{position:absolute;left:0;right:0;bottom:0;background:var(--red)}
.bands .url{position:absolute;background:var(--white);padding:0 3px;color:var(--ink)}
.url-light{position:absolute;color:var(--white);white-space:nowrap}

/* folder */
.folder{left:115px;top:81px;width:422px;height:545px;background:var(--red)}
.folder .panel{left:3px;top:150px;right:0;bottom:0;background:var(--red-soft)}
/* letterhead */
.letterhead{left:636px;top:77px;width:425px;height:550px;background:var(--white)}
/* compliment slip */
.slip{left:82px;top:671px;width:402px;height:190px;background:var(--white)}
/* envelope */
.envelope{left:84px;top:917px;width:402px;height:188px;background:var(--white)}
.envelope .flap{position:absolute;left:0;top:0;width:402px;height:62px}
/* cards */
.card-front{left:516px;top:755px;width:283px;height:165px;background:var(--red)}
.card-front .panel{left:128px;top:14px;right:0;bottom:0;background:#e3423f}
.card-back{left:516px;top:943px;width:283px;height:166px;background:var(--white)}
.card-back .name{position:absolute;left:15px;top:60px;font-size:10px;letter-spacing:.3px}
.card-back .role{position:absolute;left:15px;top:70px;font-size:8px;font-weight:700}
.card-back .lines{position:absolute;left:16px;top:84px;font-size:7.5px;line-height:1.25}
.card-back .reach{position:absolute;left:16px;top:113px;font-size:7.5px;line-height:1.3}
/* erasers */
.eraser{height:50px;border-radius:3px}
.eraser .sleeve{position:absolute;top:0;bottom:0;width:26px;right:0}
.eraser-white{left:759px;top:677px;width:128px;background:#f3f3f3}
.eraser-white .sleeve{background:#2a2a2a}
.eraser-red{left:923px;top:675px;width:130px;height:52px;background:var(--red)}
.eraser-red .sleeve{background:#f1f1f1}
/* notebook */
.notebook{left:855px;top:817px;width:211px;height:289px;background:var(--red-deep)}
.notebook .panel{left:34px;top:91px;right:0;bottom:0;background:#d83a3e}
.notebook .spiral{position:absolute;left:0;top:10px;width:18px;height:270px}
</style>
</head>
<body>

<!-- Presentation folder -->
<section class="piece folder" aria-label="Presentation folder">
  <div class="panel"></div>
  <div class="brand on-red" style="left:76px;top:89px;font-size:36px"><span class="dot" style="width:36px;height:36px"></span>VELTARO</div>
  <div class="url-light" style="left:171px;top:493px;font-size:9.5px">www.veltaro.com</div>
</section>

<!-- Letterhead -->
<section class="piece letterhead" aria-label="Letterhead">
  <div class="brand on-white" style="left:40px;top:25px;font-size:23px"><span class="dot" style="width:22px;height:22px"></span>VELTARO</div>
  <div class="contact" style="left:299px;top:16px;font-size:6.5px">
    <div>Calle Ribera 14,</div>
    <div>Puerto Alto - Ecuador EC010101</div>
    <div class="row"><svg class="ico" width="6" height="6" viewBox="0 0 10 10"><path d="M2 0h2l1 3-1.5 1a6 6 0 0 0 2.5 2.5L7 5l3 1v2c0 1-1 2-2 2A8 8 0 0 1 0 2C0 1 1 0 2 0z"/></svg>(555) 7 210-4400</div>
    <div class="row"><svg class="ico" width="6" height="5" viewBox="0 0 10 7"><rect width="10" height="7" rx="1"/></svg>info@veltaro.com</div>
  </div>
  <div class="panel" style="left:337px;top:472px;width:88px;height:193px;background:var(--blush)"></div>
  <div class="panel" style="left:370px;top:520px;width:55px;height:145px;background:var(--white)"></div>
  <div class="panel" style="left:378px;top:530px;width:47px;height:135px;background:var(--mist)"></div>
  <div class="bands" style="height:26px">
    <div class="thin" style="bottom:21px;height:2px"></div>
    <div class="thick" style="height:8px"></div>
    <div class="url" style="right:64px;bottom:15px;font-size:6.5px">www.veltaro.com</div>
  </div>
</section>

<!-- Compliment slip -->
<section class="piece slip" aria-label="Compliment slip">
  <div class="panel" style="left:253px;top:0;width:149px;height:164px;background:#f9e3e5"></div>
  <div class="panel" style="left:327px;top:80px;width:75px;height:84px;background:var(--white)"></div>
  <div class="panel" style="left:340px;top:90px;width:62px;height:74px;background:var(--mist)"></div>
  <div class="brand on-white" style="left:22px;top:23px;font-size:22px"><span class="dot" style="width:21px;height:21px"></span>VELTARO</div>
  <div class="contact" style="left:24px;top:133px;font-size:6px">
    <div>Calle Ribera 14,</div>
    <div>Puerto Alto - Ecuador EC010101</div>
    <div class="row"><svg class="ico" width="5" height="5" viewBox="0 0 10 10"><path d="M2 0h2l1 3-1.5 1a6 6 0 0 0 2.5 2.5L7 5l3 1v2c0 1-1 2-2 2A8 8 0 0 1 0 2C0 1 1 0 2 0z"/></svg>(555) 7 210-4400</div>
    <div class="row"><svg class="ico" width="5" height="4" viewBox="0 0 10 7"><rect width="10" height="7" rx="1"/></svg>info@veltaro.com</div>
  </div>
  <div class="bands" style="height:22px">
    <div class="thin" style="bottom:16px;height:2px"></div>
    <div class="thick" style="height:6px"></div>
    <div class="url" style="right:46px;bottom:11px;font-size:6px">www.veltaro.com</div>
  </div>
</section>

<!-- Envelope -->
<section class="piece envelope" aria-label="Envelope">
  <svg class="flap" viewBox="0 0 402 62" aria-hidden="true"><path d="M0 0H402L388 48Q384 62 370 62H32Q18 62 14 48Z" fill="var(--red)"/></svg>
  <div class="brand on-red" style="left:162px;top:17px;font-size:13px"><span class="dot" style="width:12px;height:12px"></span>VELTARO</div>
</section>

<!-- Business card, front -->
<section class="piece card-front" aria-label="Business card front">
  <div class="panel"></div>
  <div class="brand on-red" style="left:65px;top:70px;font-size:20px"><span class="dot" style="width:20px;height:20px"></span>VELTARO</div>
</section>

<!-- Business card, back -->
<section class="piece card-back" aria-label="Business card back">
  <div class="panel" style="left:151px;top:0;width:132px;height:134px;background:var(--blush)"></div>
  <div class="panel" style="left:219px;top:67px;width:64px;height:67px;background:var(--white)"></div>
  <div class="panel" style="left:229px;top:77px;width:54px;height:57px;background:var(--mist)"></div>
  <div class="brand on-white" style="left:16px;top:22px;font-size:19px"><span class="dot" style="width:18px;height:18px"></span>VELTARO</div>
  <div class="name">DANIEL ROJAS VERA</div>
  <div class="role">Gerente General</div>
  <div class="lines"><div>Calle Ribera 14,</div><div>Puerto Alto - Ecuador EC010101</div></div>
  <div class="reach">
    <div class="contact-row" style="display:flex;align-items:center;gap:3px"><svg class="ico" width="6" height="6" viewBox="0 0 10 10"><path d="M2 0h2l1 3-1.5 1a6 6 0 0 0 2.5 2.5L7 5l3 1v2c0 1-1 2-2 2A8 8 0 0 1 0 2C0 1 1 0 2 0z"/></svg>(555) 7 210-4400</div>
    <div class="contact-row" style="display:flex;align-items:center;gap:3px"><svg class="ico" width="6" height="7" viewBox="0 0 6 9"><path d="M1 0h4a1 1 0 0 1 1 1v7a1 1 0 0 1-1 1H1a1 1 0 0 1-1-1V1a1 1 0 0 1 1-1zm0 1.5v5.5h4V1.5z"/></svg>(555) 98 310-2277</div>
    <div class="contact-row" style="display:flex;align-items:center;gap:3px"><svg class="ico" width="6" height="5" viewBox="0 0 10 7"><rect width="10" height="7" rx="1"/></svg>drojas.veltaro.com</div>
  </div>
  <div class="bands" style="height:20px">
    <div class="thin" style="bottom:14px;height:1.5px"></div>
    <div class="thick" style="height:6px"></div>
    <div class="url" style="right:40px;bottom:10px;font-size:7px">www.veltaro.com</div>
  </div>
</section>

<!-- Erasers -->
<section class="piece eraser eraser-white" aria-label="Eraser, white">
  <div class="brand on-white" style="left:14px;top:18px;font-size:11px"><span class="dot" style="width:10px;height:10px"></span>VELTARO</div>
  <div class="sleeve"></div>
</section>
<section class="piece eraser eraser-red" aria-label="Eraser, red">
  <div class="brand on-red" style="left:17px;top:19px;font-size:11.5px"><span class="dot" style="width:11px;height:11px"></span>VELTARO</div>
  <div class="sleeve"></div>
</section>

<!-- Notebook -->
<section class="piece notebook" aria-label="Spiral notebook">
  <div class="panel"></div>
  <svg class="spiral" viewBox="0 0 18 270" aria-hidden="true">
    <g stroke="#b9b9be" stroke-width="2" fill="none">
      <path d="M2 4h14M2 16h14M2 28h14M2 40h14M2 52h14M2 64h14M2 76h14M2 88h14M2 100h14M2 112h14M2 124h14M2 136h14M2 148h14M2 160h14M2 172h14M2 184h14M2 196h14M2 208h14M2 220h14M2 232h14M2 244h14M2 256h14M2 268h14"/>
    </g>
  </svg>
  <div class="brand on-red" style="left:63px;top:25px;font-size:14px"><span class="dot" style="width:13px;height:13px"></span>VELTARO</div>
  <div class="url-light" style="left:88px;top:255px;font-size:4px;opacity:.5">www.veltaro.com</div>
</section>

</body>
</html>
```